Label Design for a Small Batch Liqueur

Need a label designed for a small batch South African liqueur known as Ter Sloek, that will be given to clients as a gift from our family owned company.

Ter Sloek is produced using brandy that is then infused with naartjies (a type of mandarin) and a selection of spices. Ter Sloek was traditionally produced in the Cape winelands in South Africa, and is supposedly named after Admiral Ter Sloek of the Nordic-West Isles Merchant company, who drank it to distraction.

The label will be placed on bottles 154mm tall and 73mm wide. More details are contained in the following link http://www.tallorvex.com.au/category/product/cat1/Beverage/cat2/Spirit/cat3/Glass/total/47/page/1/code/QX-311-5520-TB

The label must include our family surname, Kemp, as well as the liqueur name, Ter Sloek, and must have some allusion to it's South African heritage.

It Company

```html
<!DOCTYPE html>
<html lang="en">
<head>
<meta charset="utf-8">
<title>Ter Sloek Liqueur Label</title>
<link rel="stylesheet" href="https://fonts.googleapis.com/css2?family=Cinzel:wght@700;900&display=swap">
<style>
  :root {
    --page: #e9ebee;
    --gold: #d9a94a;
    --gold-light: #f6d982;
    --gold-deep: #9a6a1e;
    --label-dark: #1c0e06;
    --label-mid: #5a2f12;
    --ink: #2a1609;
    --sky-warm: #f0a040;
    --land-dark: #3a2414;
  }
  html, body {
    margin: 0;
    width: 1200px;
    height: 900px;
    overflow: hidden;
    background: var(--page);
  }
  .canvas {
    position: relative;
    width: 1200px;
    height: 900px;
  }
  .label {
    position: absolute;
    left: 380px;
    top: 80px;
    width: 440px;
    height: 740px;
  }
  .label-shape {
    position: absolute;
    inset: 0;
  }
  .label-text {
    position: absolute;
    left: 0;
    width: 440px;
    margin: 0;
    text-align: center;
    font-family: "Cinzel", "Times New Roman", serif;
    font-weight: 900;
    color: var(--gold);
    background: linear-gradient(180deg, var(--gold-light) 0%, var(--gold) 55%, var(--gold-deep) 100%);
    -webkit-background-clip: text;
    background-clip: text;
    -webkit-text-fill-color: transparent;
    line-height: 1;
  }
  .family-name {
    top: 54px;
    font-size: 32px;
    letter-spacing: 3px;
    font-weight: 700;
  }
  .product-name-line1 {
    top: 228px;
    font-size: 92px;
  }
  .product-name-line2 {
    top: 340px;
    font-size: 80px;
    letter-spacing: 1px;
  }
  .product-type {
    top: 656px;
    font-size: 30px;
    letter-spacing: 4px;
    font-weight: 700;
    background: none;
    -webkit-text-fill-color: var(--ink);
    color: var(--ink);
  }
</style>
</head>
<body>
<main class="canvas">
  <div class="label">
    <svg class="label-shape" viewBox="0 0 440 740" width="440" height="740">
      <defs>
        <radialGradient id="labelFill" cx="50%" cy="55%" r="60%">
          <stop offset="0%" stop-color="#5a2f12"/>
          <stop offset="100%" stop-color="#1c0e06"/>
        </radialGradient>
        <linearGradient id="goldBand" x1="0" y1="0" x2="0" y2="1">
          <stop offset="0%" stop-color="#f6d982"/>
          <stop offset="50%" stop-color="#d9a94a"/>
          <stop offset="100%" stop-color="#9a6a1e"/>
        </linearGradient>
        <linearGradient id="landscapeFill" x1="0" y1="0" x2="0" y2="1">
          <stop offset="0%" stop-color="#f0a040"/>
          <stop offset="55%" stop-color="#b8692a"/>
          <stop offset="100%" stop-color="#3a2414"/>
        </linearGradient>
        <linearGradient id="ornamentFill" x1="0" y1="0" x2="1" y2="0">
          <stop offset="0%" stop-color="#9a6a1e" stop-opacity="0"/>
          <stop offset="50%" stop-color="#d9a94a"/>
          <stop offset="100%" stop-color="#9a6a1e" stop-opacity="0"/>
        </linearGradient>
      </defs>

      <path class="label-body" d="M10,120 Q10,70 70,62 L150,50 Q220,8 290,50 L370,62 Q430,70 430,120 L430,660 Q430,732 358,732 L82,732 Q10,732 10,660 Z"
            fill="url(#labelFill)"/>
      <path class="label-frame" d="M34,132 Q34,92 84,86 L160,76 Q220,40 280,76 L356,86 Q406,92 406,132 L406,650 Q406,708 348,708 L92,708 Q34,708 34,650 Z"
            fill="none" stroke="url(#goldBand)" stroke-width="4"/>

      <rect class="crest-square" x="144" y="44" width="152" height="58" fill="#1c0e06" stroke="url(#goldBand)" stroke-width="3"/>

      <rect class="crest-ornament" x="70" y="114" width="300" height="40" rx="20" fill="url(#ornamentFill)" opacity="0.85"
            role="img" aria-label="Gold scrollwork ornament beneath the family crest"/>

      <rect class="heritage-landscape" x="70" y="520" width="300" height="80" fill="url(#landscapeFill)"
            role="img" aria-label="Sunset over Cape mountains and winelands"/>

      <path class="ribbon-tails" d="M40,652 L80,640 L80,700 L40,712 L56,682 Z M400,652 L360,640 L360,700 L400,712 L384,682 Z"
            fill="#9a6a1e"/>
      <rect class="ribbon-band" x="70" y="640" width="300" height="62" rx="10" fill="url(#goldBand)"/>

      <rect class="ribbon-ornament" x="180" y="610" width="80" height="20" rx="10" fill="url(#ornamentFill)"
            role="img" aria-label="Small gold flourish above the ribbon"/>
    </svg>

    <p class="label-text family-name">KEMP</p>
    <h1 class="label-text product-name-line1">TER</h1>
    <h1 class="label-text product-name-line2">SLOEK</h1>
    <p class="label-text product-type">LIQUEUR</p>
  </div>
</main>
</body>
</html>
```